Website For Custom Home Builder

-Very elegant and simple design as I am a high end custom home builder.
-I build homes $2 million to $10 million range so the website needs to reflect the level of home that I build.
-Attached are photos of homes I have built to use as well as my logo.
-I need final design to be in layered format so my local guy can edit if he needs to.

3 Page Design
1. HomePage:
-logo, some photos,
-“Building beautiful custom homes in Indianapolis for over 20 years”
2. AboutPage:
-Dean Morley has been building stunning custom homes in the Indianpolis area for over 20 years. As a small boutique building company we only build a handful of homes a year in order to offer our clients the personal attention that their homes deserve. It's this attention to detail that makes our client experience and final product something special and unique.
- family photo
3. ContactPage:
-office photo
-317-555-0192
-dean@dmbuildco.example
-415 North Larkwood Dr, Suite 310, Carmel IN 46099

Target Market(s)

Very high end clients looking to build $2 million to $10 million homes.

Industry/Entity Type

Residential high end custom home builder/construction

Coding

Coded - Design and coding required

Number of Pages Required

3 page

Requirements
Must have
• Very simple and elegant design that represents the high end homes that I build.
Nice to have
Should not have
• Should NOT have a lot of clutter or be a very busy page from a design perspective.

```html
<!DOCTYPE html>
<html lang="en">
<head>
<meta charset="utf-8">
<title>Dean Morley Custom Homes</title>
<link href="https://fonts.googleapis.com/css2?family=Outfit:wght@300;400;600;800&display=swap" rel="stylesheet">
<style>
  :root {
    --white: #ffffff;
    --footer-bg: #25292d;
    --footer-text: #6d7277;
    --accent-dark: #3a1a0b;
    --accent-light: #b55b16;
    --ceiling: #8a8a8a;
    --ceiling-dark: #6e6e6e;
    --window-green: #6f7a62;
    --wall-dark: #4a4a4c;
    --wood: #a08a6c;
    --wood-dark: #7b6a55;
    --sofa: #7d7d7d;
    --table: #c9c9c9;
    --floor: #8c8781;
  }
  * { margin: 0; padding: 0; box-sizing: border-box; }
  html, body { width: 1200px; height: 658px; overflow: hidden; }
  body { font-family: "Outfit", sans-serif; color: var(--white); background: var(--footer-bg); }
  .page { position: relative; width: 1200px; height: 658px; }

  .hero-photo {
    position: absolute; left: 0; top: 0; width: 1200px; height: 602px;
    background:
      linear-gradient(rgba(30,30,30,0.28), rgba(30,30,30,0.28)),
      radial-gradient(ellipse 130px 60px at 590px 560px, var(--table) 0%, rgba(201,201,201,0) 100%),
      radial-gradient(ellipse 420px 110px at 330px 540px, var(--sofa) 0%, rgba(125,125,125,0) 100%),
      radial-gradient(ellipse 170px 120px at 180px 360px, var(--window-green) 0%, rgba(111,122,98,0) 100%),
      radial-gradient(ellipse 180px 120px at 680px 370px, var(--window-green) 0%, rgba(111,122,98,0) 100%),
      linear-gradient(180deg, var(--ceiling) 0%, var(--ceiling-dark) 36%, rgba(74,74,76,0.0) 55%),
      linear-gradient(90deg, #9a9a9a 0%, var(--wall-dark) 30%, var(--wall-dark) 60%, var(--wood-dark) 74%, var(--wood) 88%, var(--wood-dark) 100%),
      var(--floor);
  }

  .brand {
    position: absolute; left: 84px; top: 58px; width: 140px; text-align: center;
    font-weight: 400; text-transform: uppercase; color: var(--white); line-height: 1;
  }
  .brand-name { display: block; font-size: 19px; letter-spacing: -0.3px; }
  .brand-sub { display: block; font-size: 8.5px; letter-spacing: 3.2px; margin-top: 3px; }

  .main-nav { position: absolute; top: 44px; left: 0; width: 1200px; }
  .main-nav a {
    position: absolute; font-weight: 600; font-size: 14px; letter-spacing: 4px;
    color: var(--white); text-decoration: none;
  }
  .nav-home { left: 422px; }
  .nav-about { left: 545px; }
  .nav-contact { left: 680px; }

  .social { position: absolute; top: 20px; left: 1049px; display: flex; gap: 12px; }
  .social-link {
    width: 27px; height: 27px; border-radius: 50%; background: var(--white);
    display: flex; align-items: center; justify-content: center;
  }
  .social-link svg { width: 15px; height: 15px; }

  .tagline {
    position: absolute; top: 213px; left: 0; width: 1200px; text-align: center;
    font-weight: 600; font-size: 14px; letter-spacing: 0.2px; text-transform: uppercase;
    text-shadow: 0 1px 3px rgba(0,0,0,0.5);
  }
  .headline {
    position: absolute; top: 236px; left: 0; width: 1200px; text-align: center;
    font-weight: 800; font-size: 68px; line-height: 80px; text-transform: uppercase;
    letter-spacing: 0.5px; text-shadow: 2px 3px 2px rgba(0,0,0,0.55);
  }

  .cta {
    position: absolute; left: 499px; top: 423px; width: 202px; height: 53px;
    border-radius: 5px; display: flex; align-items: center; justify-content: center;
    background: linear-gradient(90deg, var(--accent-dark), var(--accent-light));
    color: var(--white); text-decoration: none; font-weight: 600; font-size: 14px; letter-spacing: 3.5px;
  }

  .slider-arrow { position: absolute; top: 304px; width: 26px; height: 54px; }
  .slider-prev { left: 86px; }
  .slider-next { left: 1089px; }

  .site-footer {
    position: absolute; left: 0; top: 602px; width: 1200px; height: 56px; background: var(--footer-bg);
    font-size: 13px; letter-spacing: 2px; text-transform: uppercase; color: var(--footer-text);
  }
  .copyright { position: absolute; left: 86px; top: 20px; }
  .copyright strong { color: var(--white); font-weight: 600; }
  .build-info { position: absolute; right: 84px; top: 20px; }
</style>
</head>
<body>
<div class="page">
  <div class="hero-photo" role="img" aria-label="Photo of a modern living room with grey sectional sofa, white coffee table, tall garden windows and a wood-panelled wall"></div>

  <div class="brand">
    <span class="brand-name">Dean Morley</span>
    <span class="brand-sub">Custom Homes</span>
  </div>

  <nav class="main-nav">
    <a class="nav-home" href="#">HOME</a>
    <a class="nav-about" href="#">ABOUT</a>
    <a class="nav-contact" href="#">CONTACT</a>
  </nav>

  <div class="social">
    <a class="social-link" href="#" aria-label="Message us">
      <svg viewBox="0 0 16 16"><path d="M2 3h12v8H7l-3 3v-3H2z" fill="#555"/></svg>
    </a>
    <a class="social-link" href="#" aria-label="Share">
      <svg viewBox="0 0 16 16"><circle cx="4" cy="8" r="2.2" fill="#555"/><circle cx="12" cy="3.5" r="2.2" fill="#555"/><circle cx="12" cy="12.5" r="2.2" fill="#555"/><path d="M4 8L12 3.5M4 8l8 4.5" stroke="#555" stroke-width="1.4"/></svg>
    </a>
  </div>

  <p class="tagline">Building beautiful custom homes in</p>
  <h1 class="headline">Indianapolis for<br>over 20 years</h1>

  <a class="cta" href="#">CONTACT US</a>

  <svg class="slider-arrow slider-prev" viewBox="0 0 26 54" aria-label="Previous slide">
    <polyline points="25,1 1,27 25,53" fill="none" stroke="#fff" stroke-width="1.2"/>
  </svg>
  <svg class="slider-arrow slider-next" viewBox="0 0 26 54" aria-label="Next slide">
    <polyline points="1,1 25,27 1,53" fill="none" stroke="#fff" stroke-width="1.2"/>
  </svg>

  <footer class="site-footer">
    <p class="copyright">© 2023 <strong>Dean Morley</strong>. All right reserved</p>
    <p class="build-info">June 27, 2023. Layout_4</p>
  </footer>
</div>
</body>
</html>
```